Zielgruppe
Planung und Realisierung von individuellen und wertbeständigen Kamin- und Ofenlösungen, sowie Fliesen- und Baddesign.
Aufgabenstellung
Wir benötigen ein möglichst schlichtes Design für Visitenkarten, bzw. Briefpapier. Für die Visitenkarten gerne auch Vorschläge mit Prägung, Ausstanzung oder mit Heißfolie. Auch Klappkarten wären denkbar. Das Design soll "das gewisse Etwas haben" und nicht zu verspielt sein.
Die Visitenkarten sind für die Firma KARMU, das Logo von der Ausstellung "talgrund" soll dezent mit eingebunden werden (bei dem Briefpapier z.B. in der Fußzeile". Die farbliche Gestaltung sollte sich an den Farben des Logos orientieren.
Schriftart für Texte: Century Gothic
Schriftfarbe: RAL 7016
Nur eine Idee: Ich könnte mir auch gut vorstellen, dass die Visitenkarte aus einer Zündholzverpackung (wenn dann aber eine besondere mit nur einem Zündholz oder einem besonders breiten) besteht: http://lindoraversand.de/produkte_briefchen.php

```html
<!DOCTYPE html>
<html lang="de">
<head>
<meta charset="utf-8">
<title>KARMU – Visitenkarte</title>
<link rel="stylesheet" href="https://fonts.googleapis.com/css2?family=Questrial&display=swap">
<style>
  :root {
    --stage: #e9e6e1;
    --card-top: #22343b;
    --card-bottom: #15232a;
    --ink-light: #f4f4f2;
    --ink-footer: #8d989b;
    --accent: #ef8a12;
    --accent-deep: #b85f05;
    --accent-dark: #7a4200;
  }
  html, body {
    margin: 0;
    padding: 0;
    width: 1200px;
    height: 835px;
    overflow: hidden;
    background: var(--stage);
  }
  .canvas {
    position: relative;
    width: 1200px;
    height: 835px;
  }
  .fold-card {
    position: absolute;
    left: 370px;
    top: 60px;
    width: 480px;
    height: 710px;
  }
  .inner-fold {
    position: absolute;
    left: -26px;
    top: 14px;
    width: 480px;
    height: 700px;
    border-radius: 18px;
    background: linear-gradient(180deg, var(--accent) 0%, var(--accent-deep) 60%, var(--accent-dark) 100%);
    box-shadow: 0 18px 40px rgba(0, 0, 0, 0.22);
  }
  .business-card {
    position: absolute;
    left: 0;
    top: 0;
    width: 480px;
    height: 700px;
    border-radius: 18px;
    background: linear-gradient(170deg, var(--card-top) 0%, var(--card-bottom) 100%);
    box-shadow: 0 18px 40px rgba(0, 0, 0, 0.28);
    font-family: "Questrial", "Century Gothic", sans-serif;
    overflow: hidden;
  }
  .brand {
    position: absolute;
    top: 70px;
    left: 48px;
    right: 40px;
  }
  .brand-row {
    display: flex;
    align-items: center;
    gap: 16px;
  }
  .brand-name {
    margin: 0;
    font-size: 96px;
    line-height: 1;
    letter-spacing: 4px;
    font-weight: 400;
    color: var(--ink-light);
  }
  .brand-mark {
    width: 18px;
    height: 18px;
    background: var(--accent);
  }
  .brand-tagline {
    margin: 12px 0 0 4px;
    font-size: 30px;
    letter-spacing: 1px;
    color: var(--ink-light);
  }
  .die-cut-window {
    position: absolute;
    left: 286px;
    top: 250px;
    width: 150px;
    height: 330px;
    border-radius: 75px 75px 40px 40px;
    background: linear-gradient(180deg, #a8581e 0%, var(--accent-deep) 55%, var(--accent) 100%);
  }
  .partner {
    position: absolute;
    right: 40px;
    bottom: 44px;
    display: flex;
    align-items: center;
    gap: 10px;
  }
  .partner-name {
    font-size: 32px;
    color: var(--ink-footer);
    letter-spacing: 0.5px;
  }
  .partner-mark {
    width: 7px;
    height: 7px;
    background: var(--ink-footer);
  }
</style>
</head>
<body>
  <main class="canvas">
    <div class="fold-card">
      <div class="inner-fold" aria-hidden="true"></div>
      <article class="business-card">
        <header class="brand">
          <div class="brand-row">
            <h1 class="brand-name">KARMU</h1>
            <span class="brand-mark" aria-hidden="true"></span>
          </div>
          <p class="brand-tagline">kamine · öfen · fliesen</p>
        </header>
        <div class="die-cut-window" role="img" aria-label="Ausstanzung mit Blick auf die orange Innenseite der Klappkarte"></div>
        <footer class="partner">
          <span class="partner-name">talgrund</span>
          <span class="partner-mark" aria-hidden="true"></span>
        </footer>
      </article>
    </div>
  </main>
</body>
</html>
```